Notepads for Marketing pieces-BOLD design

Looking for notepads for marketing pieces with logo, phone number, and website. Maybe something faded in background. Looking for bold and different

```html
<!DOCTYPE html>
<html lang="en">
<head>
<meta charset="UTF-8">
<title>Vitalis Care Notepad</title>
<link rel="stylesheet" href="https://fonts.googleapis.com/css2?family=Lexend:wght@700;800&family=Open+Sans:wght@400&family=Arimo:wght@400&display=swap">
<style>
  :root {
    --backdrop: #c1c1c1;
    --paper: #ffffff;
    --brand-red: #ff0000;
    --ink: #111111;
    --navy: #1f3864;
    --rule: #a9a9a9;
    --faint: #fff2f2;
  }
  * { margin: 0; padding: 0; box-sizing: border-box; }
  html, body {
    width: 973px;
    height: 1200px;
    overflow: hidden;
    background: var(--backdrop);
  }
  .notepad {
    position: absolute;
    left: 76px;
    top: 20px;
    width: 820px;
    height: 1160px;
    background: var(--paper);
  }
  .watermark {
    position: absolute;
    left: 240px;
    top: 380px;
    width: 340px;
    height: 340px;
  }
  .brand-name {
    position: absolute;
    left: 84px;
    top: 68px;
    font-family: "Lexend", sans-serif;
    font-weight: 800;
    font-size: 36px;
    letter-spacing: 0.5px;
    color: var(--brand-red);
    line-height: 1;
  }
  .tagline {
    position: absolute;
    left: 66px;
    top: 131px;
    font-family: "Lexend", sans-serif;
    font-weight: 700;
    font-size: 11.5px;
    color: var(--ink);
  }
  .date-field {
    position: absolute;
    left: 586px;
    top: 66px;
    display: flex;
    align-items: flex-end;
    font-family: "Open Sans", sans-serif;
    font-size: 17px;
    color: var(--navy);
  }
  .date-field svg { margin-left: 5px; }
  .writing-rules {
    position: absolute;
    left: 57px;
    top: 0;
  }
  .contact-band {
    position: absolute;
    left: 57px;
    top: 1104px;
    width: 706px;
    height: 32px;
    background: var(--brand-red);
    display: flex;
    align-items: center;
    justify-content: center;
    gap: 8px;
    font-family: "Arimo", sans-serif;
    font-size: 14px;
    color: #ffffff;
  }
  .contact-item { display: flex; align-items: center; gap: 4px; }
</style>
</head>
<body>
  <main class="notepad">
    <svg class="watermark" viewBox="0 0 340 340" aria-hidden="true">
      <circle cx="170" cy="170" r="170" fill="var(--faint)"/>
    </svg>

    <div class="brand-name">VITALIS CARE</div>
    <p class="tagline">Home Health | Medical Staffing | Outpatient Therapy</p>

    <div class="date-field">
      <span>Date:</span>
      <svg width="134" height="20" viewBox="0 0 134 20" aria-hidden="true">
        <g stroke="var(--navy)" stroke-width="1.3" fill="none">
          <line x1="0" y1="19" x2="40" y2="19"/>
          <line x1="38" y1="19" x2="49" y2="3"/>
          <line x1="47" y1="19" x2="87" y2="19"/>
          <line x1="85" y1="19" x2="96" y2="3"/>
          <line x1="94" y1="19" x2="134" y2="19"/>
        </g>
      </svg>
    </div>

    <svg class="writing-rules" width="706" height="1070" viewBox="0 0 706 1070" aria-hidden="true">
      <g stroke="var(--rule)" stroke-width="1">
        <line x1="0" y1="226" x2="706" y2="226"/>
        <line x1="0" y1="275" x2="706" y2="275"/>
        <line x1="0" y1="324" x2="706" y2="324"/>
        <line x1="0" y1="372" x2="706" y2="372"/>
        <line x1="0" y1="421" x2="706" y2="421"/>
        <line x1="0" y1="470" x2="706" y2="470"/>
        <line x1="0" y1="519" x2="706" y2="519"/>
        <line x1="0" y1="568" x2="706" y2="568"/>
        <line x1="0" y1="617" x2="706" y2="617"/>
        <line x1="0" y1="665" x2="706" y2="665"/>
        <line x1="0" y1="714" x2="706" y2="714"/>
        <line x1="0" y1="763" x2="706" y2="763"/>
        <line x1="0" y1="812" x2="706" y2="812"/>
        <line x1="0" y1="861" x2="706" y2="861"/>
        <line x1="0" y1="909" x2="706" y2="909"/>
        <line x1="0" y1="958" x2="706" y2="958"/>
        <line x1="0" y1="1007" x2="706" y2="1007"/>
        <line x1="0" y1="1056" x2="706" y2="1056"/>
      </g>
    </svg>

    <footer class="contact-band">
      <span class="contact-item">
        <svg width="10" height="10" viewBox="0 0 24 24" aria-hidden="true"><path fill="#fff" d="M6.6 10.8a15.1 15.1 0 0 0 6.6 6.6l2.2-2.2a1 1 0 0 1 1-.25 11.4 11.4 0 0 0 3.6.57 1 1 0 0 1 1 1V20a1 1 0 0 1-1 1A17 17 0 0 1 3 4a1 1 0 0 1 1-1h3.5a1 1 0 0 1 1 1c0 1.25.2 2.45.57 3.57a1 1 0 0 1-.25 1z"/></svg>
        (555) 214-0188
      </span>
      <span class="contact-item">
        <svg width="11" height="11" viewBox="0 0 24 24" aria-hidden="true"><circle cx="12" cy="12" r="10" fill="none" stroke="#fff" stroke-width="2.4"/><path d="M2 12h20M12 2c3 3 3 17 0 20M12 2c-3 3-3 17 0 20" fill="none" stroke="#fff" stroke-width="1.8"/></svg>
        &nbsp;www.vitaliscare.org
      </span>
    </footer>
  </main>
</body>
</html>
```